Financial planning firm needs PZKL postcard invitation to workshop

We need an PZKL formatted postcard to serve as an invitation to a financial planning workshop titled Harvest Steady Gains Through Late-Life Investing With a Fresh Compass and Map.

Target Market(s)

55+ Retirement Community

Industry/Entity Type

Financial Planning

Font styles to use
Serif
Sans Serif

Requirements
Must have
• Must have PZKL formatting.
• Please make a version where the time, date, and location can be edited in Acrobat.
• Please also make an email version. If you can do html, that would be preferred.
Nice to have
• We would like the front to primarily serve as the invitation with a large picture to draw in potential clients as well as date/time/location prominently displayed along with the Holloway Advisors logo.
• PLEASE DO NOT USE THE WORD INVITATION.

```html
<!DOCTYPE html>
<html lang="en">
<head>
<meta charset="utf-8">
<title>Holloway Advisors – Workshop Postcard</title>
<link href="https://fonts.googleapis.com/css2?family=Cinzel:wght@500&family=Oswald:wght@500&family=Montserrat:wght@400;500;700&display=swap" rel="stylesheet">
<style>
  :root {
    --page-bg: #e6e8ee;
    --card-white: #ffffff;
    --brand-indigo: #3a3a9c;
    --brand-indigo-deep: #2c2a8a;
    --band-indigo: rgba(70, 68, 170, 0.88);
    --bar-black: #0c0c0e;
    --photo-light: #e9e8ec;
    --photo-mid: #b9b3ad;
    --photo-dark: #6f6a66;
    --ink: #1a1a1a;
    --text-white: #ffffff;
  }
  * { box-sizing: border-box; margin: 0; padding: 0; }
  html, body { width: 1200px; height: 1200px; overflow: hidden; }
  body {
    background: var(--page-bg);
    font-family: "Montserrat", Arial, sans-serif;
    position: relative;
  }
  .postcard {
    position: absolute;
    left: 120px;
    width: 960px;
    height: 540px;
    background: var(--card-white);
    box-shadow: 0 6px 22px rgba(20, 24, 40, 0.18);
    overflow: hidden;
  }
  .postcard--front { top: 40px; }
  .postcard--back { top: 620px; }

  /* Front */
  .front-photo {
    position: absolute; inset: 0;
    background:
      radial-gradient(ellipse at 62% 40%, var(--photo-mid) 0%, transparent 45%),
      radial-gradient(ellipse at 22% 75%, var(--photo-dark) 0%, transparent 35%),
      linear-gradient(120deg, var(--photo-light) 0%, #d8d4d0 55%, #a9a29c 100%);
  }
  .brand-mark {
    position: absolute; left: 36px; top: 44px;
    display: flex; align-items: center; gap: 10px;
    color: var(--brand-indigo);
    font-family: "Cinzel", Georgia, serif;
    font-weight: 500;
    font-size: 26px;
    letter-spacing: 1px;
  }
  .brand-mark__square {
    width: 28px; height: 28px; background: var(--brand-indigo);
  }
  .headline-band {
    position: absolute; left: 86px; top: 262px;
    width: 560px; height: 190px;
    background: var(--band-indigo);
    padding: 30px 30px;
    display: flex; align-items: center;
  }
  .headline {
    font-family: "Oswald", "Arial Narrow", sans-serif;
    font-weight: 500;
    font-size: 32px;
    line-height: 1.14;
    text-transform: uppercase;
    color: var(--text-white);
    letter-spacing: 0.3px;
  }
  .event-bar {
    position: absolute; left: 0; right: 0; bottom: 0;
    height: 66px;
    background: var(--bar-black);
    display: flex; align-items: center; justify-content: space-between;
    padding: 0 40px;
    color: var(--text-white);
    font-size: 19px;
    font-weight: 500;
  }

  /* Back */
  .back-panel {
    position: absolute; left: 0; top: 0; bottom: 0;
    width: 640px;
    background: linear-gradient(180deg, #eceaf2 0%, #c9c6dc 35%, #6a66bd 58%, var(--brand-indigo-deep) 78%, var(--brand-indigo-deep) 100%);
  }
  .back-copy {
    position: absolute; left: 34px; right: 34px; bottom: 34px;
    color: var(--text-white);
    font-size: 13.5px;
    line-height: 1.5;
  }
  .back-copy p + p { margin-top: 14px; }
  .back-copy strong { font-weight: 700; display: block; }
  .indicia {
    position: absolute; right: 40px; top: 34px;
    width: 82px; height: 66px;
    border: 1.5px solid var(--ink);
    font-size: 8.5px; line-height: 1.2;
    text-align: center;
    padding-top: 8px;
    color: var(--ink);
    font-family: Arial, sans-serif;
  }
  .indicia b { font-weight: 700; }
  .address-box {
    position: absolute; right: 40px; bottom: 70px;
    width: 250px; height: 96px;
    border: 1.5px solid var(--ink);
    padding: 40px 20px 0;
    font-family: Arial, sans-serif;
    font-size: 14px; line-height: 1.3;
    color: var(--ink);
  }
</style>
</head>
<body>
  <section class="postcard postcard--front">
    <div class="front-photo" role="img" aria-label="Photo of a senior couple meeting with a financial advisor on a sofa"></div>
    <div class="brand-mark">
      <span class="brand-mark__square"></span>
      <span class="brand-mark__name">HOLLOWAY ADVISORS</span>
    </div>
    <div class="headline-band">
      <h1 class="headline">Harvest Steady Gains Through Late-Life Investing With a Fresh Compass and Map</h1>
    </div>
    <div class="event-bar">
      <span class="event-bar__date">Date: September,18th</span>
      <span class="event-bar__time">Time: 6:30pm</span>
      <span class="event-bar__location">Location: Ashford Hall</span>
    </div>
  </section>

  <section class="postcard postcard--back">
    <div class="back-panel" role="img" aria-label="Photo of a smiling senior couple reviewing documents with an advisor, fading into indigo">
      <div class="back-copy">
        <p>Neil will discuss how cookiecutter portfolios can result in lackluster performance amid higher risk and how to avoid this by putting together an investment portfolio that improves your overall financial security and fulfills your legacy goals.</p>
        <p><strong>An Accredited Wealth Guide you can trust.</strong>Neil Holloway is an Accredited Wealth Guide and Fiduciary specializing in asset management of IRA, retirement, investment, and trust accounts. Holloway Advisors, LLC is an independent Registered Investment Advisor with a low cost, commission-free business model.</p>
      </div>
    </div>
    <div class="indicia">PRSRT STD<br>ECRWSS<br>U.S. POSTAGE<br><b>PAID</b><br>PZKL RETAIL</div>
    <div class="address-box">Local<br>Postal Customer</div>
  </section>
</body>
</html>
```